Window Cleaning Flyer targeting body corporates

Need a flyer for window cleaning targeting body corporate (approx A5 print size). It should be professional and match the logo attached.
We are looking to standout but not be to over the top for a window cleaning/services company.
We want to entice the receptionist or managers to call us because they see no good reason not to.

Industry/Entity Type

Window Cleaning

Font styles to use
Serif

Colors
0555a3
fbed22

Requirements
Must have
• Professional with a few of the photos attached included. Must include logo and the following contact details:
• Ph: 9413 6570
• email: admin@brightpaneworks.com.au
• PO Box 4726
• Marlowe Heights
• 3284
Nice to have
• Colours matching logo/ van print layout. Looking for more of a simplistic professional design.
Should not have
• Cartoon pictures, animated decorations or stock photos.

```html
<!DOCTYPE html>
<html lang="en">
<head>
<meta charset="utf-8">
<title>Brightpane Window Cleaning – Body Corporate Flyer</title>
<link href="https://fonts.googleapis.com/css2?family=Archivo+Black&family=Arimo:wght@400;700&display=swap" rel="stylesheet">
<style>
  :root {
    --navy: #0555a3;
    --navy-deep: #0a4d96;
    --yellow: #fbed22;
    --white: #ffffff;
    --sky: #5d92d8;
    --sky-mid: #4f86cf;
    --foam: #dfe6ee;
    --shadow-grey: #3b3d40;
    --page: #1a1a1a;
  }
  * { box-sizing: border-box; margin: 0; padding: 0; }
  html, body { width: 1200px; height: 1200px; overflow: hidden; background: var(--page); }
  .flyer {
    position: absolute; left: 212px; top: 50px;
    width: 632px; height: 897px;
    transform: scale(1.2266); transform-origin: top left;
    background: var(--navy); overflow: hidden;
    font-family: "Arimo", Arial, sans-serif; color: var(--white);
  }
  .top-band { position: absolute; left: 0; top: 0; width: 100%; height: 8px; background: var(--yellow); }
  .hero-photo {
    position: absolute; left: 0; top: 8px; width: 100%; height: 590px;
    background:
      radial-gradient(ellipse 120px 150px at 560px 330px, rgba(59,61,64,.85) 0%, rgba(59,61,64,0) 100%),
      radial-gradient(ellipse 260px 40px at 180px 80px, rgba(223,230,238,.75) 0%, rgba(223,230,238,0) 100%),
      radial-gradient(ellipse 300px 45px at 160px 430px, rgba(223,230,238,.7) 0%, rgba(223,230,238,0) 100%),
      radial-gradient(ellipse 90px 260px at 520px 300px, rgba(223,230,238,.55) 0%, rgba(223,230,238,0) 100%),
      radial-gradient(ellipse at 35% 40%, var(--sky) 0%, var(--sky-mid) 50%, #8fb2e2 100%);
  }
  .chevron { position: absolute; left: 0; top: 0; width: 632px; height: 897px; }
  .logo-box {
    position: absolute; left: 374px; top: 8px; width: 227px; height: 130px;
    background: var(--navy-deep); text-align: center; padding-top: 34px;
  }
  .logo-name { font-weight: 700; font-size: 30px; color: var(--yellow); letter-spacing: 1px; }
  .logo-web { margin-top: 30px; font-size: 12px; color: var(--yellow); letter-spacing: .3px; }
  .call-now {
    position: absolute; left: 62px; top: 222px;
    font-family: "Archivo Black", "Arial Black", sans-serif; font-size: 37px; line-height: 37px;
    color: var(--yellow); text-shadow: 2px 2px 0 var(--navy-deep);
  }
  .job-photo { position: absolute; }
  .job-photo--wash { left: 48px; top: 494px; width: 123px; height: 246px; background: linear-gradient(180deg, #8a9290 0%, #6f7774 55%, #a9aca6 100%); }
  .job-photo--pole { left: 177px; top: 562px; width: 122px; height: 245px; background: linear-gradient(180deg, #9a7550 0%, #4a4f55 50%, #6f8a4a 100%); }
  .quote-cta {
    position: absolute; left: 48px; top: 816px; width: 265px;
    font-weight: 700; font-size: 15px; line-height: 16px; color: var(--yellow);
  }
  .contact-details {
    margin-top: 4px; font-size: 9.5px; line-height: 12px; color: var(--white);
  }
  .info { position: absolute; left: 338px; top: 548px; width: 238px; }
  .info h2 { font-weight: 400; font-size: 17px; line-height: 22px; }
  .info h2 .accent { color: var(--yellow); }
  .info p { font-weight: 700; font-size: 11.4px; line-height: 15px; }
  .info p + p { margin-top: 8px; }
  .info .specialty { margin-top: 10px; }
  .services { list-style: none; margin-top: 14px; }
  .services li { position: relative; padding-left: 19px; font-weight: 700; font-size: 11.4px; line-height: 15px; margin-bottom: 9px; }
  .services svg { position: absolute; left: 0; top: 2px; width: 11px; height: 11px; }
  .foot-bar { position: absolute; left: 338px; top: 881px; width: 236px; height: 16px; background: var(--yellow); }
</style>
</head>
<body>
<div class="flyer">
  <div class="hero-photo" role="img" aria-label="Photo: squeegee wiping soapy foam from a window, worker behind the glass"></div>

  <svg class="chevron" viewBox="0 0 632 897" aria-hidden="true">
    <polygon fill="#fbed22" points="0,563 412,470 632,570 632,897 0,897"/>
    <polygon fill="#0555a3" points="0,590 412,492 632,592 632,897 0,897"/>
  </svg>

  <div class="top-band"></div>

  <div class="logo-box">
    <div class="logo-name">BRIGHTPANE</div>
    <div class="logo-web">www.brightpaneworks.com.au</div>
  </div>

  <div class="call-now">CALL NOW<br>9413 6570</div>

  <div class="job-photo job-photo--wash" role="img" aria-label="Photo: team member pressure washing a concrete driveway"></div>
  <div class="job-photo job-photo--pole" role="img" aria-label="Photo: team member cleaning building windows with a water-fed pole"></div>

  <div class="quote-cta">Contact the Brightpane Team for an easy, FREE quote today!<br>Dial: 9413 6570
    <div class="contact-details">admin@brightpaneworks.com.au<br>PO Box 4726, Marlowe Heights 3284</div>
  </div>

  <div class="info">
    <h2>Let <span class="accent">Brightpane</span> Take Care</h2>
    <p>of your body corporate needs! With over 15 years of experience we will ensure the job is completed to the highest standard everytime.</p>
    <p>Most Importantly, Brightpane Window Cleaning take pride in being friendly and courteous to all residents.</p>
    <h2 class="specialty">Brightpane specialises in Body Corporate</h2>
    <ul class="services">
      <li><svg viewBox="0 0 24 24"><polygon fill="#fbed22" points="12,1 15,9 23,9 17,14 19,23 12,18 5,23 7,14 1,9 9,9"/></svg>Window Cleaning</li>
      <li><svg viewBox="0 0 24 24"><polygon fill="#fbed22" points="12,1 15,9 23,9 17,14 19,23 12,18 5,23 7,14 1,9 9,9"/></svg>Gutter Cleaning (using our ladder free gutter vacuum)</li>
      <li><svg viewBox="0 0 24 24"><polygon fill="#fbed22" points="12,1 15,9 23,9 17,14 19,23 12,18 5,23 7,14 1,9 9,9"/></svg>Pressure Washing including moss treatment to prevent mould regrowth on concrete surface</li>
    </ul>
  </div>

  <div class="foot-bar"></div>
</div>
</body>
</html>
```